Milo Castell Moving DL Flyer

We need a double sided DL flyer to give to patients to let them know that we are moving location.
On one side we would like it to read:
"We Are Moving!" and "November 2017" and our logo.
On the other side we would like it to read:
"Same Great Staff"
"Same Great Service"
"Bigger, Brighter and Better"
"New Location at 42 Quarry Rd"
with a map below (attached)
The flyer should follow our practice branding. Attached is a copy of our business card as an example of this.

```html
<!DOCTYPE html>
<html lang="en">
<head>
<meta charset="utf-8">
<title>Milo Castell Optometry – Moving DL Flyer</title>
<link rel="stylesheet" href="https://fonts.googleapis.com/css2?family=Open+Sans:wght@300;400;600;700;800&display=swap">
<style>
  :root {
    --plum: #4f3b5c;
    --plum-soft: #6b5778;
    --ink: #1e1e1e;
    --grey: #8c8c8c;
    --grey-light: #c9c9c9;
    --paper: #ffffff;
    --stage: #666666;
    --photo-a: #e9d8c8;
    --photo-b: #b98a6c;
    --map-dark: #2a2a2a;
    --map-pink: #e98a8c;
  }
  * { box-sizing: border-box; margin: 0; padding: 0; }
  html, body { width: 1200px; height: 850px; overflow: hidden; }
  body {
    background: var(--stage);
    font-family: "Open Sans", Arial, sans-serif;
    position: relative;
  }

  .flyer {
    position: absolute;
    top: 70px;
    width: 300px;
    height: 636px;
    background: var(--paper);
    overflow: hidden;
    box-shadow: 0 10px 24px rgba(0,0,0,.35);
  }
  .flyer--front { left: 235px; }
  .flyer--back  { left: 665px; }

  .side-label {
    position: absolute;
    top: 730px;
    width: 300px;
    text-align: center;
    color: #fff;
    font-size: 30px;
    font-weight: 400;
  }
  .side-label--front { left: 235px; }
  .side-label--back  { left: 665px; }

  /* brand lockup */
  .brand {
    display: flex;
    align-items: center;
    gap: 10px;
  }
  .brand__mark {
    width: 12px; height: 12px;
    background: var(--plum);
  }
  .brand__text { line-height: 1.05; }
  .brand__name { font-size: 13px; font-weight: 400; color: var(--ink); }
  .brand__field { font-size: 24px; font-weight: 700; color: var(--ink); letter-spacing: -.3px; }
  .brand__tagline { font-size: 11px; color: var(--plum); margin-top: 2px; }

  /* front */
  .front__header { height: 112px; padding: 34px 0 0 34px; }
  .front__art { position: absolute; top: 100px; left: 0; width: 300px; height: 536px; }
  .front__copy {
    position: absolute;
    left: 0; right: 0; top: 410px;
    text-align: center;
    color: #fff;
  }
  .headline {
    display: flex;
    justify-content: center;
    align-items: flex-end;
    font-weight: 800;
    line-height: .9;
    text-transform: uppercase;
  }
  .headline__we { font-size: 44px; }
  .headline__stack { display: flex; flex-direction: column; align-items: flex-start; margin-left: 3px; }
  .headline__are { font-size: 18px; color: var(--grey-light); font-weight: 700; }
  .headline__moving { font-size: 36px; }
  .move-date { font-size: 27px; font-weight: 800; margin-top: 8px; letter-spacing: .3px; }
  .move-date__year { color: var(--grey); }
  .web-line {
    display: flex; align-items: center; justify-content: center; gap: 10px;
    font-size: 16px; font-weight: 700; margin-top: 26px;
  }
  .web-line::before, .web-line::after {
    content: ""; width: 44px; height: 1px; background: currentColor; opacity: .7;
  }

  /* back */
  .back__header { padding: 30px 0 0 64px; }
  .back__header .brand__field { font-size: 20px; }
  .back__header .brand__name { font-size: 11px; }
  .back__header .brand__tagline { font-size: 9px; }
  .map-frame { position: relative; margin: 16px auto 0; width: 250px; height: 150px; }
  .map-frame__bracket {
    position: absolute; top: 0; width: 18px; height: 150px;
    border: 6px solid var(--grey-light);
  }
  .map-frame__bracket--left { left: 0; border-right: none; }
  .map-frame__bracket--right { right: 0; border-left: none; }
  .map {
    position: absolute; left: 30px; top: 10px; width: 190px; height: 130px;
    background: linear-gradient(135deg, #d8d8d8 0%, #bdbdbd 45%, var(--map-pink) 46%, var(--map-pink) 70%, #c4c4c4 71%);
    border: 8px solid var(--map-dark);
  }
  .tags { display: flex; justify-content: center; gap: 14px; margin-top: 22px; }
  .tag {
    background: var(--plum);
    color: #fff;
    border-radius: 6px;
    padding: 4px 10px;
    text-align: center;
    line-height: 1.05;
    text-transform: uppercase;
  }
  .tag__light { display: block; font-size: 13px; font-weight: 300; }
  .tag__bold { display: block; font-size: 14px; font-weight: 700; }
  .slogan {
    text-align: center; text-transform: uppercase; font-weight: 800;
    color: var(--plum); font-size: 22px; line-height: 1.05; margin-top: 14px;
  }
  .slogan__and { color: var(--grey); }
  .location { text-align: center; margin-top: 14px; }
  .location__pill {
    display: inline-block; background: var(--plum); color: #fff;
    font-size: 11px; letter-spacing: 1px; text-transform: uppercase;
    padding: 2px 22px; border-radius: 5px;
  }
  .location__pin { display: block; margin: 8px auto 2px; }
  .location__address {
    display: inline-block; border: 1px solid var(--ink);
    font-size: 13px; font-weight: 700; padding: 3px 22px; text-transform: uppercase;
    color: var(--ink);
  }
  .back .web-line { color: var(--ink); margin-top: 18px; font-size: 14px; }
</style>
</head>
<body>

  <section class="flyer flyer--front" aria-label="Flyer front">
    <header class="front__header">
      <div class="brand">
        <span class="brand__mark"></span>
        <div class="brand__text">
          <div class="brand__name">Milo Castell</div>
          <div class="brand__field">Optometry</div>
          <div class="brand__tagline">See Better. See Us.</div>
        </div>
      </div>
    </header>

    <svg class="front__art" viewBox="0 0 300 536" aria-hidden="false">
      <defs>
        <linearGradient id="photoTone" x1="0" y1="0" x2="1" y2="1">
          <stop offset="0" stop-color="var(--photo-a)"/>
          <stop offset="1" stop-color="var(--photo-b)"/>
        </linearGradient>
      </defs>
      <path d="M0 40 Q160 -10 300 30 L300 536 L0 536 Z" fill="var(--plum)"/>
      <path d="M0 70 Q140 10 300 44 L300 250 Q150 300 0 290 Z" fill="url(#photoTone)" role="img" aria-label="Photograph of an optometrist examining a patient's eyes"/>
      <path d="M0 290 Q150 300 300 250 L300 262 Q150 318 0 308 Z" fill="var(--paper)"/>
    </svg>

    <div class="front__copy">
      <div class="headline">
        <span class="headline__we">We</span>
        <span class="headline__stack">
          <span class="headline__are">Are</span>
          <span class="headline__moving">Moving!</span>
        </span>
      </div>
      <div class="move-date">NOVEMBER <span class="move-date__year">2017</span></div>
      <div class="web-line">www.milocastell.com.au</div>
    </div>
  </section>

  <section class="flyer flyer--back back" aria-label="Flyer back">
    <header class="back__header">
      <div class="brand">
        <span class="brand__mark"></span>
        <div class="brand__text">
          <div class="brand__name">Milo Castell</div>
          <div class="brand__field">Optometry</div>
          <div class="brand__tagline">See Better. See Us.</div>
        </div>
      </div>
    </header>

    <div class="map-frame">
      <span class="map-frame__bracket map-frame__bracket--left"></span>
      <div class="map" role="img" aria-label="Street map showing the new practice location"></div>
      <span class="map-frame__bracket map-frame__bracket--right"></span>
    </div>

    <div class="tags">
      <div class="tag"><span class="tag__light">Same Great</span><span class="tag__bold">Service</span></div>
      <div class="tag"><span class="tag__light">Same Great</span><span class="tag__bold">Staff</span></div>
    </div>

    <h2 class="slogan">Bigger, Brighter<br><span class="slogan__and">and</span> Better</h2>

    <div class="location">
      <span class="location__pill">New Location</span>
      <svg class="location__pin" width="18" height="18" viewBox="0 0 24 24" aria-hidden="true">
        <circle cx="12" cy="12" r="11" fill="none" stroke="var(--ink)" stroke-width="1.5"/>
        <path d="M12 5a4.5 4.5 0 0 0-4.5 4.5C7.5 13 12 19 12 19s4.5-6 4.5-9.5A4.5 4.5 0 0 0 12 5z" fill="var(--ink)"/>
        <circle cx="12" cy="9.5" r="1.6" fill="#fff"/>
      </svg>
      <span class="location__address">42 Quarry Rd</span>
    </div>

    <div class="web-line">www.milocastell.com.au</div>
  </section>

  <div class="side-label side-label--front">Front</div>
  <div class="side-label side-label--back">Back</div>

</body>
</html>
```